Branding for Rēvāla Cider a new Tasmanian cider company

We are a new Tasmanian cider business looking for a logo/label design to be used on our 330ml cider bottle labels and as a logo.
We want our cider label to pop and stand out from the rest.
As our cider is a Tasmanian product we would like it to appear as a premium product.
I have attached pictures of all of the other Tasmanian Cider labels to give an idea of what we are competing with NOT because we like the designs!!!

We are yet to start advertising our business so it is all an open slab, we have no starting point just a few ideas that have been listed below in the "Nice to Haves" section.

This brief has been updated as what we originally requested was too similar to other labels already in production so didn't give our product an edge.

The label size will be approx 80mm x 125mm

Target Market(s)

Craft cider market, bottle shops, boutique bars and restaurants

Font styles to use
Serif
Decorative
Script

Colors

Designer to choose colors to be used in the design.

Requirements
Must have
• The words
• "Rēvāla Cider" with the diacritic's over the o's
• "Tasmanian Made"
• or
• "Made in Tasmania"
• The Tasmanian part can be in all caps if it looks better
Nice to have
• All or some of the below incorporated into the label:
• Rēvāla was the goddess of fruit trees, gardens, and orchards.
• She watched over and protected fruit trees
• She was thought to be a wood nymph which are usually represented as beautiful, young girls.
• We would like our label to possibly incorporate the above.
• Maybe a wood nymph/goddess in an apple/pear orchard or against an apple/pear tree.
• Maybe no tree, just the nymph/goddess holding fruit.
• Maybe an apple/pear branch with a nympy/goddess under it.
• I have attached a few images from findora of wood nymphs and fruit goddess' for inspiration. Not sure if realistic or animated would look best, but if animated, not cartoon like as we would like a premium look. Possibly similar to the attached Wrenfold Cider artwork
• We will have 3 types of cider; Apple, Pear and Apple & Strawberry so essentially 3 labels, maybe the apple tree could change to a pear tree and for the apple & strawberry cider maybe strawberries growing under the apple tree?
• All just ideas, we are open to :)
• If you think something else will suit the name, please feel free to submit it

```html
<!DOCTYPE html>
<html lang="en">
<head>
<meta charset="utf-8">
<title>Rēvāla Cider – Label</title>
<link rel="stylesheet" href="https://fonts.googleapis.com/css2?family=Cinzel:wght@400&family=Montserrat:wght@300;400&display=swap">
<style>
  :root {
    --backdrop: #e6e3e4;
    --label-gold: #e3b23c;
    --label-cream: #f3f2f0;
    --fruit-gold: #d9a430;
    --fruit-shade: #c8921f;
    --ink-light: #fbf6e8;
  }
  html, body {
    margin: 0;
    padding: 0;
    width: 1200px;
    height: 900px;
    overflow: hidden;
    background: var(--backdrop);
  }
  .canvas {
    width: 1200px;
    height: 900px;
    display: flex;
    align-items: center;
    justify-content: center;
  }
  .cider-label {
    width: 480px;
    height: 626px;
    display: block;
  }
  .label-title {
    font-family: "Cinzel", serif;
    font-size: 36px;
    fill: var(--ink-light);
    letter-spacing: 1px;
  }
  .label-origin {
    font-family: "Montserrat", sans-serif;
    font-weight: 300;
    font-size: 14px;
    letter-spacing: 6px;
    fill: var(--ink-light);
  }
  .label-volume {
    font-family: "Montserrat", sans-serif;
    font-weight: 300;
    font-size: 14px;
    fill: var(--ink-light);
  }
  .label-volume-small {
    font-size: 9px;
    letter-spacing: 0.5px;
  }
</style>
</head>
<body>
<main class="canvas">
  <svg class="cider-label" viewBox="0 0 460 600" xmlns="http://www.w3.org/2000/svg" aria-label="Rēvāla Cider bottle label">
    <defs>
      <clipPath id="label-shape">
        <ellipse cx="230" cy="300" rx="230" ry="300"/>
      </clipPath>
      <radialGradient id="fruit-tone" cx="40%" cy="40%" r="65%">
        <stop offset="0%" stop-color="var(--label-gold)"/>
        <stop offset="100%" stop-color="var(--fruit-shade)"/>
      </radialGradient>
    </defs>

    <g clip-path="url(#label-shape)">
      <rect class="label-body" x="0" y="0" width="460" height="600" fill="var(--label-gold)"/>
      <path class="label-crown" d="M0,0 H460 V140 Q230,310 0,140 Z" fill="var(--label-cream)"/>
    </g>

    <ellipse class="label-rule" cx="230" cy="300" rx="219" ry="289" fill="none" stroke="var(--ink-light)" stroke-width="1.2"/>

    <ellipse class="fruit-artwork" role="img" aria-label="Illustration of a golden pear with a green leaf"
             cx="230" cy="118" rx="44" ry="56" fill="url(#fruit-tone)"/>

    <text class="label-title" x="230" y="385" text-anchor="middle">Rēvāla Cider</text>
    <text class="label-origin" x="233" y="410" text-anchor="middle">TASMANIAN</text>
    <text class="label-volume" x="230" y="510" text-anchor="middle">330ml&#160;&#160;8% <tspan class="label-volume-small">ALC/VOL</tspan></text>
  </svg>
</main>
</body>
</html>
```